Law Firm Needs a Stationery Design

We need a stationery design for a law firm based in the East African region called 'Mbweteka Olinyo & Company Advocates'. We are a law firm specializing in commercial, public and constitutional law. Our practice areas include Telecommunications Law, Mining Law, Oil and Energy Law, Real Estate and Land Development Law, Employment Law, Family Law, Civil and Criminal Litigation, Constitutional Law, Company Secretariat and more. We represent a wide variety of clients, ranging from individuals to corporations and approach each case with full attention, dedication and legal acumen in order to protect the interests of our clients. The final stationary design should communicate innovation and expertise to meet our clients’ legal needs.
Target Market(s)
New clients, current and former clients, other lawyers in and outside of our practice area, or other professionals, contacts and centers of influence within the region
Industry/Entity Type
Real Estate
Colors
Designer to choose colors to be used in the design.
Look and feel
Each slider illustrates characteristics of the customer's brand and the style your logo design should communicate.

```html
<!DOCTYPE html>
<html lang="en">
<head>
<meta charset="utf-8">
<title>Mbweteka Olinyo &amp; Company Advocates — Stationery</title>
<link rel="stylesheet" href="https://fonts.googleapis.com/css2?family=Maven+Pro:wght@400;500&family=Tinos&display=swap">
<style>
  :root {
    --slate: #37424c;
    --slate-soft: #4a5560;
    --grey: #8d939a;
    --paper: #ffffff;
    --ground: #ffffff;
    --footer-text: #9aa3ab;
    --shadow: 4px 6px 10px rgba(0,0,0,.35);
  }
  * { box-sizing: border-box; margin: 0; padding: 0; }
  html, body { width: 1200px; height: 1200px; overflow: hidden; background: var(--ground); }
  .canvas { position: relative; width: 1200px; height: 1200px; font-family: "Maven Pro", sans-serif; color: var(--slate); }
  .sheet { position: absolute; background: var(--paper); box-shadow: var(--shadow); overflow: hidden; }

  .wordmark { display: flex; align-items: center; gap: 7px; color: var(--slate); font-weight: 400; line-height: 1.15; }
  .wordmark .mark { width: 12px; height: 12px; background: currentColor; flex: none; }
  .wordmark--stack { flex-direction: column; text-align: center; gap: 8px; }

  /* Letterhead */
  .letterhead { left: 49px; top: 110px; width: 521px; height: 740px; }
  .letterhead .wordmark { position: absolute; left: 0; right: 0; top: 36px; font-size: 10px; }
  .letter-body { position: absolute; left: 58px; right: 46px; top: 166px; font-family: "Tinos", serif; font-size: 11.6px; line-height: 12.7px; color: #222; }
  .letter-body p { margin-bottom: 0; text-align: left; }
  .letter-body .salutation { margin-bottom: 16px; }
  .letter-body .sign-off { margin-top: 30px; }
  .letter-footer { position: absolute; left: 0; right: 0; bottom: 0; height: 60px; background: var(--slate); color: var(--footer-text); font-size: 10px; line-height: 14.5px; text-align: center; padding-top: 6px; }

  /* Back sheet */
  .letter-back { left: 608px; top: 44px; width: 524px; height: 244px; }
  .letter-back .wordmark { position: absolute; left: 28px; top: 30px; font-size: 8px; width: 110px; }
  .letter-back .address { position: absolute; left: 28px; top: 104px; font-size: 6.6px; line-height: 9px; color: var(--grey); }

  /* Envelope */
  .envelope { left: 652px; top: 211px; width: 498px; height: 300px; overflow: visible; box-shadow: none; background: none; }
  .envelope svg { position: absolute; left: 0; top: 0; filter: drop-shadow(4px 6px 6px rgba(0,0,0,.35)); }
  .envelope .wordmark { position: absolute; left: 200px; top: 150px; font-size: 7.5px; width: 120px; }

  /* Compliment slip */
  .comp-slip { left: 612px; top: 576px; width: 523px; height: 246px; }
  .comp-slip .greeting { position: absolute; left: 29px; top: 164px; font-size: 17px; color: var(--slate-soft); }
  .comp-slip .wordmark { position: absolute; right: 30px; top: 28px; font-size: 8.5px; width: 120px; }
  .comp-slip .contact { position: absolute; right: 30px; top: 130px; text-align: right; font-size: 8px; line-height: 10.5px; color: var(--grey); }
  .comp-slip .contact span { display: block; }
  .comp-slip .contact .gap { margin-top: 10px; }
  .comp-slip .band { position: absolute; left: 0; right: 0; bottom: 0; height: 46px; background: var(--slate); }

  /* Logo variants */
  .variant { position: absolute; top: 947px; width: 174px; height: 173px; display: flex; align-items: center; justify-content: center; padding: 12px; }
  .variant .wordmark { font-size: 13px; }
  .variant--grey { left: 50px; background: var(--slate); }
  .variant--grey .wordmark { color: #a7adb3; }
  .variant--light { left: 226px; background: var(--paper); }
  .variant--white { left: 398px; background: var(--slate); }
  .variant--white .wordmark { color: #ffffff; }

  /* Business cards */
  .card { position: absolute; width: 114px; height: 198px; background: var(--slate); box-shadow: var(--shadow); }
  .card--front { left: 758px; top: 902px; transform: rotate(-11deg); }
  .card--front .wordmark { position: absolute; left: 10px; top: 60px; width: 96px; color: #8f979e; font-size: 9px; }
  .card--back { left: 888px; top: 896px; width: 137px; color: #fff; text-align: center; font-size: 6.6px; }
  .card--back .person { margin-top: 38px; font-size: 8px; font-weight: 500; }
  .card--back .email { margin-top: 18px; }
  .card--back .address { margin-top: 30px; line-height: 9px; color: #c8cdd2; }
  .card--back .phone { margin-top: 12px; color: #c8cdd2; }
  .card--back .mark { position: absolute; left: 61px; bottom: 18px; width: 14px; height: 14px; background: #56616b; }
</style>
</head>
<body>
<main class="canvas">

  <section class="sheet letterhead" aria-label="Letterhead">
    <div class="wordmark wordmark--stack"><span class="mark"></span><span>Mbweteka Olinyo &amp;<br>Company Advocates</span></div>
    <div class="letter-body">
      <p class="salutation">Dear Sir,</p>
      <p>Iquid et, ad magnitae recto tem remque aut ad molorest, sae. Untotatis am, si nos quost, nem quam fuga. Estore doluptat eum velignihit et volore aut harum et vera quam nus atur, sundae parumet rem enihillestem adi te voluptatem doloren dandae et ene nus ut eos mi, sitatiaeped mil incimusapel escia idiossit faceri venienihit offic tem quodion sedipisit vo loratem qui quam expedi aut apitaqu atesererum erum laborerferi ulpa simet exped que vidunt ariaspe enis perunt litaepe rionecto blaborerum quatusae lignihicatus sit am, ut por aut ma voluptaqui ipicitaerci imolumqui deruptateste magnatibus as utaesedi velectes etum voles evelitio. At moloreptae. Nam et vellabo ribus, od estrumquam fugia as ducim alistis as nonet pro officae et, consece pudissi musciis susam fugit doloreseque lamuscit iminctu resteturi omnia conesed mollorior aut dellestis dolo velit andita con pos de am velit vel il ipicabo riatior uptaturem estiunt, imos magnihil il inum quam aut dolori di ut in rercipsae ommolor aut accaepernam, aut magnimet, tempe eumendae rereritate mo dolorate et quo occum et accus alisqui ilibus magnam vel idici aut omnisquam natet untum rerum eos inciis es eos dit, voloreptis etur ad molor solo el ilit quas assime liquam same molor maximillat quis num inusdae catusap elluptat.</p>
      <p>Iminctotae volenderum dolupta ssunto omnihil iatur, omnihicia dolo ipis minverrore qui of ficiis alitae sanimi, sam raepe quossum imus molorro bea nitisimolent eum quiatis a voleni hic tes receatibus amusdaeprae. Ita quia venem. Itatiur moluptatur, coreiun tecaborpore ve lent pratio. Ut odignimus autem atus samentium digenisscia con ni blab illesenis nosaperum arum et undem simenis id et es doluptium faccus, ilitatius dolupta quaepud itionsedio voluptatibus volupti dipicae voluptate audipic tem namenim agnieni squam, est quam con re nonsend esequos remporem et litatii storum fuga. Nam et la di occulparibus viduciaeped moluptatquas resere nonsecat.</p>
      <p class="sign-off">Kind Regards,</p>
    </div>
    <footer class="letter-footer">
      Plot 7-9 Nsambya Lane, Kololo, Kampala, Uganda<br>
      +256 300 555 018<br>
      info@mbwetekaolinyo.com
    </footer>
  </section>

  <section class="sheet letter-back" aria-label="Continuation sheet">
    <div class="wordmark"><span class="mark"></span><span>Mbweteka Olinyo &amp; Company Advocates</span></div>
    <p class="address">Plot 7-9 Nsambya Lane,<br>Kololo, Kampala, Uganda</p>
  </section>

  <section class="sheet envelope" aria-label="DL envelope">
    <svg width="498" height="300" viewBox="0 0 498 300">
      <rect x="0" y="55" width="498" height="245" fill="#ffffff"/>
      <polygon points="20,0 478,0 498,42 470,110 28,110 0,42" fill="#37424c" role="img" aria-label="Envelope flap lined with a repeating brand pattern in slate tones"/>
    </svg>
    <div class="wordmark"><span class="mark"></span><span>Mbweteka Olinyo &amp; Company Advocates</span></div>
  </section>

  <section class="sheet comp-slip" aria-label="Compliment slip">
    <div class="wordmark"><span class="mark"></span><span>Mbweteka Olinyo &amp; Company Advocates</span></div>
    <p class="greeting">with compliments</p>
    <p class="contact">
      <span>Plot 7-9 Nsambya Lane,</span>
      <span>Kololo, Kampala, Uganda</span>
      <span class="gap">+256 300 555 018</span>
      <span>info@mbwetekaolinyo.com</span>
    </p>
    <div class="band"></div>
  </section>

  <div class="variant variant--grey"><div class="wordmark"><span class="mark"></span><span>Mbweteka Olinyo &amp; Company Advocates</span></div></div>
  <div class="variant variant--light"><div class="wordmark"><span class="mark"></span><span>Mbweteka Olinyo &amp; Company Advocates</span></div></div>
  <div class="variant variant--white"><div class="wordmark"><span class="mark"></span><span>Mbweteka Olinyo &amp; Company Advocates</span></div></div>

  <section class="card card--front" aria-label="Business card front">
    <div class="wordmark"><span class="mark"></span><span>Mbweteka Olinyo &amp; Company Advocates</span></div>
  </section>
  <section class="card card--back" aria-label="Business card back">
    <p class="person">Daniel Mbweteka</p>
    <p class="email">info@mbwetekaolinyo.com</p>
    <p class="address">Plot 7-9 Nsambya Lane,<br>Kololo, Kampala, Uganda</p>
    <p class="phone">+256 300 555 018</p>
    <span class="mark"></span>
  </section>

</main>
</body>
</html>
```